Plumbing and Fire Protection Consulting Engineering

Business Cards for one person plumbing and fire protection engineering consulting business based in NJ, serving mostly New York City:
RVT Advisory, Plumbing and Fire Protection Engineering
Daniel Korvinsky- President
52-17 Maple Terrace, Glen Rock, NJ 07452
201-486-2173
rvtpipework@mailbox-example.com

Target Market(s)

- Private Building Developers, looking to reduce construction cost
- MEP (Mechanical, Electrical, Plumbing) Design Engineers that have staff shortage, need temporary help, advise, drawings quality control
- Architects that need advise on plumbing or fire protection
- Any of the above that need opinion on disputed construction costs, change orders, construction observation reports

Industry/Entity Type

Business

Contact Information for Business Card

Logo and business card should include (other suggestions welcome):
- A plumbing symbol, like pipe or wrench or similar
- Fire Protection symbol, like fire sprinkler
- Dollar signs $$$$$ in descending font sizes suggesting construction cost reduction as a result of my work. or some other symbol of economic design
- Symbol of engineering
- High rise building(s) or Manhattan skyline on the background, maybe building under construction.
- Maybe a building floor plan design (preferably old, not modern, like in Michelangelo or Gaudi sketches)

Font styles to use
Sans Serif

Colors

Designer to choose colors to be used in the design.

Requirements
Must have
• A card that is unique, unlike any others- like my business is.
• My name, business name, address, phone, email, see description
Nice to have
• Something that suggests 30+ years experience in this field, not sure how to convey this message.
• Maybe my Linkedin picture with Statue of Liberty on the background (attached) is good to have, but i am not sure- not insisting on that.
Should not have
• Symbols that not related to engineering design and construction- like fire truck, funny plumbers figures and symbols, toilets, etc.
• Computer symbols. I am not trying to impress clients with my computer skills, not my selling point

```html
<!DOCTYPE html>
<html lang="en">
<head>
<meta charset="utf-8">
<title>RVT Advisory – Business Cards</title>
<link href="https://fonts.googleapis.com/css2?family=Open+Sans:wght@400;600;700&family=Oswald:wght@700&display=swap" rel="stylesheet">
<style>
  :root {
    --backdrop: #262626;
    --kraft-light: #d8b98f;
    --kraft-mid: #c4a070;
    --kraft-dark: #a8814f;
    --ink: #2a2622;
    --rule: rgba(42, 38, 34, 0.45);
  }
  * { box-sizing: border-box; margin: 0; padding: 0; }
  html, body {
    width: 1200px; height: 900px; overflow: hidden;
    background: var(--backdrop);
    font-family: "Open Sans", Arial, sans-serif;
    color: var(--ink);
  }
  .stage { position: relative; width: 1200px; height: 900px; }
  .card {
    position: absolute; top: 306px;
    width: 440px; height: 272px;
    background: linear-gradient(135deg, var(--kraft-light) 0%, var(--kraft-mid) 50%, var(--kraft-dark) 100%);
  }
  .card--front { left: 149px; }
  .card--back { left: 608px; }

  .brand { position: absolute; left: 0; right: 0; text-align: center; }
  .brand__mark {
    display: block; margin: 0 auto;
    border-radius: 50%; background: var(--ink);
  }
  .brand__name {
    font-family: "Oswald", "Arial Narrow", sans-serif;
    font-weight: 700; text-transform: uppercase;
    letter-spacing: 0.3px; line-height: 1; white-space: nowrap;
  }
  .brand__tagline {
    font-family: "Oswald", "Arial Narrow", sans-serif;
    font-weight: 700; text-transform: uppercase;
    letter-spacing: 0.6px; line-height: 1; white-space: nowrap;
  }

  .card--front .brand { top: 20px; }
  .card--front .brand__mark { width: 62px; height: 62px; }
  .card--front .brand__name { font-size: 32px; margin-top: 14px; }
  .card--front .brand__tagline { font-size: 9.5px; margin-top: 3px; }

  .card--back .brand { top: 62px; }
  .card--back .brand__mark { width: 82px; height: 82px; }
  .card--back .brand__name { font-size: 38px; margin-top: 14px; }
  .card--back .brand__tagline { font-size: 11.5px; margin-top: 3px; }

  .person {
    position: absolute; right: 226px; top: 187px; text-align: right;
  }
  .person__name { font-size: 14px; font-weight: 600; text-transform: uppercase; letter-spacing: 0.2px; white-space: nowrap; }
  .person__title { font-size: 11.5px; margin-top: 2px; }

  .divider {
    position: absolute; left: 224px; top: 175px;
    width: 1px; height: 72px; background: var(--rule);
  }

  .contact { position: absolute; left: 233px; top: 173px; font-size: 10.5px; white-space: nowrap; }
  .contact__line { display: flex; align-items: center; gap: 6px; height: 17px; }
  .contact__icon { width: 8px; height: 8px; fill: var(--ink); flex: none; }
  .contact__address { margin-top: 4px; font-size: 12.5px; line-height: 1.45; }
</style>
</head>
<body>
<main class="stage">
  <section class="card card--front" aria-label="Business card front">
    <div class="brand">
      <span class="brand__mark"></span>
      <div class="brand__name">RVT Advisory</div>
      <div class="brand__tagline">Plumbing &amp; Fire Protection Engineering</div>
    </div>

    <div class="person">
      <div class="person__name">Daniel Korvinsky</div>
      <div class="person__title">President</div>
    </div>

    <div class="divider"></div>

    <div class="contact">
      <div class="contact__line">
        <svg class="contact__icon" viewBox="0 0 8 8" aria-hidden="true">
          <path d="M1.8 0h4.4a.8.8 0 0 1 .8.8v6.4a.8.8 0 0 1-.8.8H1.8a.8.8 0 0 1-.8-.8V.8A.8.8 0 0 1 1.8 0zm.4 1v5h3.6V1z"/>
        </svg>
        <span>201-486-2173</span>
      </div>
      <div class="contact__line">
        <svg class="contact__icon" viewBox="0 0 8 8" aria-hidden="true">
          <path d="M0 1.5h8v5H0z"/>
          <path d="M0.6 2l3.4 2.4L7.4 2" fill="none" stroke="#c4a070" stroke-width="0.8"/>
        </svg>
        <span>rvtpipework@mailbox-example.com</span>
      </div>
      <div class="contact__address">52-17 Maple Terrace,<br>Glen Rock, NJ 07452</div>
    </div>
  </section>

  <section class="card card--back" aria-label="Business card back">
    <div class="brand">
      <span class="brand__mark"></span>
      <div class="brand__name">RVT Advisory</div>
      <div class="brand__tagline">Plumbing &amp; Fire Protection Engineering</div>
    </div>
  </section>
</main>
</body>
</html>
```